Poster for the "Songs of the tides" concert

We need a poster for the concert: May 31, June 2 Songs of Tides.
In Program:Halvorsen: Symphony No. 3 (Vestra)Dombrevnik String Symphony No. 8Concert program exploring music that reflected milestone events of social change. Lumenari will present pieces that inspired or expressed progress, equality, human rights, and all human values we now take for granted.
Fri. May 31 / 8 pm / New Britain Grace Hill Meeting House Fellowship (417 Pellham Rd)Sun. June 2 / 2 pm / Hartford Thornbury Galleria Museum of Art (215 Elm Row)

Target Market(s)

Classical music audience, sophisticated

Colors

Designer to choose colors to be used in the design.

Requirements
Must have
• Songs of Tides
• In Program:
• Halvorsen: Symphony No. 3 (Vestra)
• Dombrevnik String Symphony No. 8
• Feldin: Sinfonia Concertante for Violin and Viola
• Orsolya Kendrek, violin, Matthias Ordell, viola, conductor
• Concert program exploring music that reflected milestone events of social change.
• Lumenari will present pieces that inspired or expressed progress, equality, human rights.
• Fri. May 31 / 8 pm / New Britain
• Grace Hill Meeting House Fellowship (417 Pellham Rd)
• Sun. June 2 / 2 pm / Hartford
• Thornbury Galleria Museum of Art (215 Elm Row)
• www.thelumenari.org
• Phone: (860) 471-PLMR (7567)

```html
<!DOCTYPE html>
<html lang="en">
<head>
<meta charset="utf-8">
<title>Songs of Tides — Concert Poster</title>
<link href="https://fonts.googleapis.com/css2?family=Poppins:wght@700;800&family=Montserrat:wght@400&display=swap" rel="stylesheet">
<style>
  :root {
    --poster-red: #c13234;
    --deep-red: #7a1c1e;
    --ink: #111111;
    --paper: #ffffff;
  }
  html, body { margin: 0; padding: 0; overflow: hidden; }
  body { width: 848px; height: 1200px; background: var(--poster-red); }
  .poster {
    position: relative; width: 848px; height: 1200px; overflow: hidden;
    background: var(--poster-red); color: var(--paper);
    font-family: "Poppins", sans-serif; font-weight: 800; text-transform: uppercase;
  }
  .artwork {
    position: absolute; inset: 0;
    background: radial-gradient(ellipse 70% 55% at 25% 85%, rgba(17,17,17,0.55), rgba(17,17,17,0) 70%),
                radial-gradient(ellipse 45% 35% at 85% 30%, rgba(17,17,17,0.35), rgba(17,17,17,0) 70%);
  }
  .title {
    position: absolute; top: 132px; left: 0; width: 848px; margin: 0;
    text-align: center; font-size: 72px; line-height: 54px; letter-spacing: -1.5px;
  }
  .event { position: absolute; margin: 0; }
  .event--friday { left: 238px; top: 272px; }
  .event--sunday { left: 234px; top: 484px; }
  .event__line { display: block; font-size: 44px; line-height: 50px; letter-spacing: -0.5px; }
  .event__venue {
    display: block; margin-top: 4px; font-size: 16.5px; line-height: 20px; font-weight: 700; letter-spacing: -0.3px;
  }
  .program { position: absolute; top: 694px; left: 0; width: 848px; text-align: center; }
  .program__heading { margin: 0 0 12px; font-size: 40px; line-height: 50px; letter-spacing: -0.5px; }
  .program__list { list-style: none; margin: 0; padding: 0; }
  .program__item { font-size: 19px; line-height: 35px; font-weight: 700; letter-spacing: -0.3px; }
  .program__performers {
    margin: 2px 0 0; font-size: 15px; line-height: 20px; font-weight: 700; letter-spacing: 0;
  }
  .about {
    position: absolute; top: 890px; left: 0; width: 848px; margin: 0; text-align: center;
    font-family: "Montserrat", sans-serif; font-weight: 400; text-transform: none;
    font-size: 19px; line-height: 25px;
  }
  .about span { display: block; }
  .about .gap { margin-top: 5px; }
  .contact {
    position: absolute; top: 1022px; left: 0; width: 848px; margin: 0; text-align: center;
    font-size: 20px; line-height: 25px; font-weight: 800; letter-spacing: -0.3px;
  }
  .contact span { display: block; }
</style>
</head>
<body>
<main class="poster">
  <div class="artwork" role="img"
       aria-label="Illustration area: black silhouette of a figure with a megaphone and swirling musical notes on red"></div>

  <h1 class="title">Songs of<br>Tides</h1>

  <p class="event event--friday">
    <span class="event__line">Fri. May 31</span>
    <span class="event__line">8 pm</span>
    <span class="event__line">New Britain</span>
    <span class="event__venue">Grace Hill Meeting House Fellowship<br>(417 Pellham Rd)</span>
  </p>

  <p class="event event--sunday">
    <span class="event__line">Sun. June 2</span>
    <span class="event__line">2 pm</span>
    <span class="event__line">Hartford</span>
    <span class="event__venue">Thornbury Galleria Museum of Art<br>(215 Elm Row)</span>
  </p>

  <section class="program">
    <h2 class="program__heading">In Program</h2>
    <ul class="program__list">
      <li class="program__item">Halvorsen: Symphony No. 3 (Vestra)</li>
      <li class="program__item">Dombrevnik String Symphony No. 8</li>
      <li class="program__item">Feldin: Sinfonia Concertante for Violin and Viola</li>
    </ul>
    <p class="program__performers">Orsolya Kendrek, violin · Matthias Ordell, viola, conductor</p>
  </section>

  <p class="about">
    <span>Concert program exploring music</span>
    <span>that reflected milestone events of social change</span>
    <span class="gap">Lumenari will present pieces that inspired or expressed</span>
    <span>progress, equality, human rights</span>
  </p>

  <p class="contact">
    <span>www.thelumenari.org</span>
    <span>Phone: (860) 471-PLMR (7567)</span>
  </p>
</main>
</body>
</html>
```